Wordpress web design

We need a website buil in using Wordpress with 5 pages.

Pages: HOME SERVICES GALLERY TESTIMONIALS CONTACT US ABOUT US.

We are looking for a unique, professional and clean web for our construction company.

Company name: TALL OAK BUILDING SERVICES. We can olso provide you with the logo. Please don't use any flashin, intro, or any ready templates.

All your ideas are welcome.

Many thanks,
Dorian

Target Market(s)

Construction

Industry/Entity Type

Construction

Font styles to use
Sans Serif
Decorative

Requirements
Must have
• Connect with construction and London
Nice to have
• Nice and clean

```html
<!DOCTYPE html>
<html lang="en">
<head>
<meta charset="utf-8">
<title>Tall Oak Building Services</title>
<link href="https://fonts.googleapis.com/css2?family=Raleway:wght@400;500;600&family=Open+Sans:wght@400;600&display=swap" rel="stylesheet">
<style>
:root{
  --orange:#f26522;
  --orange-light:#f7931e;
  --orange-deep:#e8501c;
  --ink:#2a2226;
  --text:#555;
  --muted:#777;
  --rule:#dcdcdc;
  --footer:#000;
  --btn-dark:#3a2314;
  --white:#fff;
}
*{margin:0;padding:0;box-sizing:border-box}
html,body{width:967px;height:1200px;overflow:hidden;background:var(--white)}
body{position:relative;font-family:'Open Sans',sans-serif;color:var(--text)}
.abs{position:absolute}
.backdrop{left:0;top:102px;width:967px;height:290px;background:linear-gradient(#e6e6e6,#f4f4f4 60%,#fff)}
.brand{left:160px;top:12px;display:flex;align-items:center;gap:8px}
.brand-mark{width:50px;height:50px;background:var(--orange)}
.brand-name{font-family:'Raleway',sans-serif;font-weight:500;font-size:15px;line-height:17px;color:var(--orange)}
.contact{right:163px;top:33px;text-align:right;font-family:'Raleway',sans-serif}
.contact-label{font-size:12px;color:var(--orange)}
.contact-phone{font-size:15px;color:var(--ink);display:flex;align-items:center;gap:4px;justify-content:flex-end}
.nav{left:158px;top:75px;width:651px;height:33px;display:flex;background:linear-gradient(var(--orange-light),var(--orange-deep))}
.nav a{display:flex;align-items:center;justify-content:center;color:var(--white);text-decoration:none;font-family:'Raleway',sans-serif;font-weight:500;font-size:11.5px;border-right:1px solid rgba(255,255,255,.35)}
.nav a:last-child{border-right:none}
.hero{left:158px;top:108px;width:651px;height:303px;background:linear-gradient(120deg,#b9cde0,#dfe6ec 45%,#c9c3b6)}
.hero-caption{left:195px;top:198px;width:256px;height:110px;background:rgba(30,30,30,.82);padding:20px 21px;color:var(--white)}
.hero-caption h2{font-family:'Raleway',sans-serif;font-weight:400;font-size:21px;line-height:24px}
.hero-caption p.lead{font-family:'Raleway',sans-serif;font-size:12px;margin-top:2px}
.hero-caption p.small{font-size:7px;line-height:12px;color:#aaa;margin-top:6px}
.dots{left:458px;top:386px;display:flex;gap:3px}
.dots span{width:11px;height:11px;border-radius:50%;background:rgba(255,255,255,.85)}
.about{left:160px;top:448px;width:649px;text-align:center}
.about h1{font-family:'Raleway',sans-serif;font-weight:500;font-size:24px;color:var(--ink)}
.about .lead{font-size:10px;color:#444;margin-top:5px}
.about .body{font-size:7.2px;line-height:13.5px;color:var(--muted);margin:10px 25px 0}
.divider{left:160px;top:578px;width:649px;height:1px;background:var(--rule)}
.service{width:200px}
.service-photo{width:198px;height:97px}
.service h3{font-family:'Raleway',sans-serif;font-weight:500;font-size:15px;color:var(--ink);margin-top:8px}
.service p{font-size:7.2px;line-height:12.7px;color:var(--muted);margin-top:2px}
.btn{display:inline-flex;align-items:center;justify-content:center;height:20px;width:70px;font-size:7.5px;color:var(--white);border-radius:2px;margin-top:10px;background:linear-gradient(var(--orange-light),var(--orange-deep))}
.band{left:0;top:818px;width:967px;height:282px}
.gallery-text{left:171px;top:896px;width:280px;color:var(--white)}
.gallery-text h2{font-family:'Raleway',sans-serif;font-weight:400;font-size:22px}
.gallery-text .lead{font-size:9px;line-height:13.5px;margin-top:8px}
.gallery-text .body{font-size:7.8px;line-height:13.5px;margin-top:6px;opacity:.9}
.btn-dark{background:var(--btn-dark);width:69px;height:21px;margin-top:10px}
.thumb{border:2px solid var(--white)}
.footer{left:0;top:1100px;width:967px;height:100px;background:var(--footer)}
.footer-links{left:160px;top:1126px;font-family:'Raleway',sans-serif;font-size:8.5px;color:var(--white)}
.footer-links span{margin:0 3px}
.copyright{left:160px;top:1147px;font-size:7.8px;color:#666}
.social{left:750px;top:1124px;display:flex;gap:4px}
.social span{width:14px;height:14px;background:var(--white);border-radius:2px}
</style>
</head>
<body>
<div class="abs backdrop"></div>

<header>
  <div class="abs brand">
    <div class="brand-mark"></div>
    <div class="brand-name">TALL OAK<br>BUILDING SERVICES</div>
  </div>
  <div class="abs contact">
    <div class="contact-label">Contact Us</div>
    <div class="contact-phone">
      <svg width="12" height="12" viewBox="0 0 24 24"><path fill="#555" d="M6.6 10.8a15.2 15.2 0 0 0 6.6 6.6l2.2-2.2a1 1 0 0 1 1-.25 11.4 11.4 0 0 0 3.6.57 1 1 0 0 1 1 1V20a1 1 0 0 1-1 1A17 17 0 0 1 3 4a1 1 0 0 1 1-1h3.5a1 1 0 0 1 1 1c0 1.25.2 2.45.57 3.57a1 1 0 0 1-.25 1z"/></svg>
      555.014.2290
    </div>
  </div>
  <nav class="abs nav">
    <a style="width:87px">HOME</a>
    <a style="width:101px">SERVICES</a>
    <a style="width:99px">GALLERY</a>
    <a style="width:133px">TESTIMONIALS</a>
    <a style="width:118px">CONTACT US</a>
    <a style="width:113px">ABOUT US</a>
  </nav>
</header>

<section>
  <div class="abs hero" role="img" aria-label="Two engineers in hard hats reviewing building plans on a construction site"></div>
  <div class="abs hero-caption">
    <h2>Construction Services</h2>
    <p class="lead">Cum sociis natoque penatibus</p>
    <p class="small">Vivamus porttitor purus nisi eleifend libero a tempus libero lectus feugiat felis Morbi diam mauris viver</p>
  </div>
  <div class="abs dots"><span></span><span></span><span></span><span></span></div>
</section>

<section class="abs about">
  <h1>ABOUT TALL OAK BUILDING SERVICES</h1>
  <p class="lead">Pellentesque faucibus Ut accumsan ultricies elit Maecenas at justo id velit placerat molestie</p>
  <p class="body">Curabitur iaculis tempus eros Curabitur vel mi sit amet magna malesuada ultrices Ut nisi erat fermentum vel congue id euismod in elit Fusce ultricies orci ac feugiat suscipit leo massa sodales velit et scelerisque mi tortor at ipsum cligula augue bibendum accumsan vestibulum ut commodo a mi Morbi ornare gravida elit Integer congue augue et malesuada iaculis ipsum dui aliquet felis at cursus magna nisl nec elit Praesent elementum elit at tellus nec ultricies sit amet porttitor matti</p>
</section>
<div class="abs divider"></div>

<section>
  <article class="abs service" style="left:159px;top:606px">
    <div class="service-photo" role="img" aria-label="High-rise buildings under construction with tower cranes" style="background:linear-gradient(160deg,#1e4fa0,#6f8fc0 55%,#c9c7c2)"></div>
    <h3>Featured Service</h3>
    <p>Aaolutpat Etiam est nunc venenatis in tristique eu impe rdiet ac nisl Cum sociis natoque penatibus nisl Cum sociis natoque penatibus se quam leo molestie</p>
    <span class="btn">READ MORE</span>
  </article>
  <article class="abs service" style="left:386px;top:606px">
    <div class="service-photo" role="img" aria-label="Team in yellow hard hats studying plans around a table" style="background:linear-gradient(150deg,#c9a46a,#e8c030 45%,#4a3a2c)"></div>
    <h3>Featured Service</h3>
    <p>Aaolutpat Etiam est nunc venenatis in tristique eu impe rdiet ac nisl Cum sociis natoque penatibus nisl Cum sociis natoque penatibus se quam leo molestie</p>
    <span class="btn">READ MORE</span>
  </article>
  <article class="abs service" style="left:610px;top:606px">
    <div class="service-photo" role="img" aria-label="Concrete tower frame with a crane at dusk" style="background:linear-gradient(120deg,#2d3236,#5b6770 50%,#9aa6ac)"></div>
    <h3 style="margin-top:6px">Featured Service</h3>
    <p>Aaolutpat Etiam est nunc venenatis in tristique eu impe rdiet ac nisl Cum sociis rdiet ac nisl Cum sociis natoque penatibus se quam leo molestie sed luctus quis</p>
    <span class="btn">READ MORE</span>
  </article>
</section>

<section>
  <svg class="abs band" viewBox="0 0 967 282" role="img" aria-label="Orange band with faint skyscraper imagery">
    <defs>
      <linearGradient id="bandFill" x1="0" y1="0" x2="1" y2="1">
        <stop offset="0" stop-color="#f36f21"/>
        <stop offset=".5" stop-color="#f7941d"/>
        <stop offset="1" stop-color="#f26522"/>
      </linearGradient>
    </defs>
    <polygon points="0,50 967,0 967,282 0,282" fill="url(#bandFill)"/>
  </svg>
  <div class="abs gallery-text">
    <h2>Our Gallery</h2>
    <p class="lead">Atrices Ut nisi erat fermentum vel congue id euismod in elit Fusce ultricies orci ac feugiat suscipit leo</p>
    <p class="body">et scelerisque mi tortor at ipsum cligula augue bibendum accumsan vestibulum ut commodo a mi Morbi ornare gravida elit Integer congue augue et malesuada iaculis ipsum dui aliquet felis</p>
    <span class="btn btn-dark">VIEW MORE</span>
  </div>
  <div class="abs thumb" role="img" aria-label="Two-storey house at dusk" style="left:500px;top:888px;width:147px;height:93px;background:linear-gradient(#3f67b5,#8fa8d0 60%,#a89a86)"></div>
  <div class="abs thumb" role="img" aria-label="Modern house with lawn and mountain view" style="left:653px;top:888px;width:147px;height:93px;background:linear-gradient(#7aa7d8,#b9c9c9 50%,#6c8d3c)"></div>
  <div class="abs thumb" role="img" aria-label="Modern glass building facade" style="left:500px;top:987px;width:95px;height:68px;background:linear-gradient(135deg,#1f5fc0,#e9eef3 60%,#5d8ec8)"></div>
  <div class="abs thumb" role="img" aria-label="Glass office tower" style="left:599px;top:987px;width:70px;height:68px;background:linear-gradient(#2f7fd0,#6aa8e0)"></div>
  <div class="abs thumb" role="img" aria-label="Contemporary villa lit at night" style="left:673px;top:987px;width:127px;height:68px;background:linear-gradient(#23338a,#4c5bb0 60%,#c9c5d2)"></div>
</section>

<footer>
  <div class="abs footer"></div>
  <div class="abs footer-links">HOME<span>|</span>SERVICES<span>|</span>GALLERY<span>|</span>TESTIMONIALS<span>|</span>CONTACT US<span>|</span>ABOUT US</div>
  <div class="abs copyright">© 2015 Company Name &nbsp;All right reserved &nbsp;Term of Use</div>
  <div class="abs social" aria-label="Social links"><span></span><span></span><span></span></div>
</footer>
</body>
</html>
```